IT Company looking to market towards Dental Offices

I am looking for a full-color design. Using my existing logo. Must have High Res stock photos. The brochure needs to be full page edge to edge design single fold pamphlet style. Content provided. Please see the website in attached Word Doc for more content.

```html
<!DOCTYPE html>
<html lang="en">
<head>
<meta charset="utf-8">
<title>Byteline Tech – Dental Services Brochure</title>
<link href="https://fonts.googleapis.com/css2?family=Montserrat:wght@600;700;800&family=Open+Sans:wght@400;600&display=swap" rel="stylesheet">
<style>
  :root{
    --navy:#0b2a7a;
    --blue:#1b78c8;
    --sky:#2f8fe0;
    --grey:#d9dbdf;
    --paper:#ffffff;
    --ink:#2d3440;
    --dark:#2b2c2f;
    --bg:#eceded;
  }
  *{box-sizing:border-box;margin:0;padding:0}
  html,body{width:705px;height:1200px;overflow:hidden;background:var(--bg)}
  body{font-family:"Open Sans",Arial,sans-serif;color:var(--ink);position:relative}
  .page{position:absolute;left:132px;width:440px;height:570px;background:var(--paper);overflow:hidden;box-shadow:0 4px 14px rgba(0,0,0,.18)}
  .page--front{top:20px}
  .page--back{top:610px}

  /* front */
  .hero-photo{position:absolute;left:0;top:0;width:100%;height:350px;
    background:linear-gradient(160deg,#cfe9e0 0%,#9fd1c2 45%,#d8efe9 70%,#8fcfd0 100%)}
  .brand-tab{position:absolute;left:0;top:36px;width:172px;height:56px;background:linear-gradient(#f3f4f6,var(--grey));
    border:3px solid var(--sky);border-left:none;border-radius:0 0 26px 0;display:flex;align-items:center;gap:8px;padding-left:16px}
  .brand-mark{width:14px;height:14px;background:var(--navy);border-radius:50%}
  .brand-name{font-family:"Montserrat",Arial,sans-serif;font-weight:700;font-size:17px;color:var(--navy)}
  .intro{position:absolute;left:26px;top:370px;width:300px}
  .intro h1{font-family:"Montserrat",Arial,sans-serif;font-weight:800;font-size:19px;color:var(--navy);margin-bottom:6px}
  .intro p{font-size:8.2px;line-height:1.45;text-align:justify}
  .web-band{position:absolute;right:0;top:470px;width:160px;height:46px}
  .web-band span{position:absolute;right:14px;top:16px;font-family:"Montserrat",Arial,sans-serif;font-weight:600;font-size:9px;color:#fff}
  .base-band{position:absolute;left:0;bottom:0;width:100%;height:24px;background:var(--navy);border-top:3px solid var(--sky)}

  /* back */
  .services-title{position:absolute;top:18px;width:100%;text-align:center;font-family:"Montserrat",Arial,sans-serif;font-weight:700;font-size:15px;color:var(--ink);letter-spacing:.5px}
  .service-grid{position:absolute;left:22px;top:46px;width:396px;display:grid;grid-template-columns:1fr 1fr;gap:8px}
  .box{border:2px solid var(--blue);border-radius:6px;overflow:hidden;background:#fff}
  .box h2{background:var(--blue);color:#fff;font-family:"Montserrat",Arial,sans-serif;font-size:7.5px;font-weight:700;padding:3px 7px}
  .box ul,.box p{font-size:7px;line-height:1.45;padding:4px 8px}
  .box ul{list-style:none}
  .box li::before{content:"\2022  ";color:var(--blue)}
  .box--wide{grid-column:1 / span 2}
  .vault-zone{position:absolute;left:0;top:245px;width:100%;height:301px;background:linear-gradient(135deg,#3a3b3e,var(--dark) 60%,#1d1e20)}
  .vault-photo{position:absolute;left:20px;top:110px;width:180px;height:180px;border-radius:50%;background:radial-gradient(circle,#e4e6ea,#a7abb2 60%,#6f737a)}
  .vault-copy{position:absolute;left:210px;top:20px;width:210px;color:#fff}
  .vault-copy h2{font-family:"Montserrat",Arial,sans-serif;font-weight:800;font-size:17px;color:var(--sky);margin-bottom:6px}
  .vault-copy p{font-size:7.6px;line-height:1.5;margin-bottom:8px}
  .back-band{position:absolute;left:0;bottom:0;width:100%;height:24px;background:var(--navy);border-top:3px solid var(--sky)}
  .back-band span{position:absolute;left:22px;top:5px;font-family:"Montserrat",Arial,sans-serif;font-weight:600;font-size:8.5px;color:#fff}
</style>
</head>
<body>

<section class="page page--front">
  <div class="hero-photo" role="img" aria-label="Photo of a bright dental treatment room with chair, overhead light and monitor"></div>
  <div class="brand-tab"><span class="brand-mark"></span><span class="brand-name">Byteline Tech</span></div>
  <div class="intro">
    <h1>DENTAL SERVICES</h1>
    <p>Byteline Tech offers proven expertise in Dental Practices. We have trained engineers that specialize in Dental practices. We can handle supporting your Practice Management Software to installing IOCs, Remote &amp; Sensors, Pano's, X-rays, scanners, and pen pads. Being familiar with the Digital side of how your practice runs we will be able to predict and plan for your growth by providing the correct configurations and storage needs you will require. We know DentaCore!</p>
  </div>
  <svg class="web-band" viewBox="0 0 160 46" aria-hidden="true">
    <polygon points="14,0 160,0 160,46 0,46" fill="#0b2a7a"/>
    <line x1="14" y1="0" x2="0" y2="46" stroke="#2f8fe0" stroke-width="3"/>
  </svg>
  <div class="web-band"><span>www.maplegrovetech.com</span></div>
  <div class="base-band"></div>
</section>

<section class="page page--back">
  <h1 class="services-title">OUR SERVICES</h1>
  <div class="service-grid">
    <div class="box"><h2>HARDWARE SALES</h2>
      <ul><li>Workstations</li><li>Servers</li><li>Printers</li><li>Networking</li><li>Sensors &amp; Scanners</li></ul></div>
    <div class="box"><h2>INFRASTRUCTURE</h2>
      <ul><li>Network Design</li><li>Cabling &amp; Wiring</li><li>Backup Systems</li><li>Firewall Setup</li><li>Wireless Access</li></ul></div>
    <div class="box"><h2>SOLUTIONS</h2>
      <p>Remote monitoring and help desk support for every workstation in your office.</p></div>
    <div class="box"><h2>READY TO MAKE YOUR TECHNOLOGY WORK?</h2>
      <p>Call us today for a free review of your office network and imaging systems.</p></div>
    <div class="box box--wide"><h2>ABOUT US</h2>
      <p>We are a local team of certified technicians who have served dental offices for many years with fast and friendly support.</p></div>
  </div>
  <div class="vault-zone">
    <div class="vault-photo" role="img" aria-label="Photo of a round steel bank vault door"></div>
    <div class="vault-copy">
      <h2>TOOTHSAFE.COM</h2>
      <p>Secure offsite backup built for dental records. Your patient data stays encrypted and ready to restore whenever you need it.</p>
      <p>Our team checks every backup daily so you never lose a single chart or image.</p>
    </div>
  </div>
  <div class="back-band"><span>www.maplegrovetech.com</span></div>
</section>

</body>
</html>
```